Lirelle Home Fragrance

I am looking to create a brand for my home fragrance line ( diffusers and candles). Looking for designs (logo) that will go on the diffuser bottle as well as the packaging for these.

Target Market(s)

online

Industry/Entity Type

Home Improvement

Font styles to use
Other font styles liked:
• Not sure what it's called, but something vintage. similar to the attached photo

Colors

Designer to choose colors to be used in the design.

Requirements
Must have
• Attractive packages

```html
<!DOCTYPE html>
<html lang="en">
<head>
<meta charset="utf-8">
<title>Lirelle Home Fragrance – English Rose Label</title>
<link href="https://fonts.googleapis.com/css2?family=Josefin+Sans:wght@300;400&display=swap" rel="stylesheet">
<style>
  :root {
    --backdrop: #e5e5e5;
    --label: #ffffff;
    --frame: #b39273;
    --ink: #2b2b2b;
    --ink-soft: #555050;
    --ornament: #c9ab8c;
  }
  * { margin: 0; padding: 0; box-sizing: border-box; }
  html, body {
    width: 1200px; height: 1200px; overflow: hidden;
    background: var(--backdrop);
    font-family: "Josefin Sans", sans-serif;
  }
  .canvas {
    width: 1200px; height: 1200px;
    display: flex; align-items: center; justify-content: center;
  }
  .label {
    width: 720px; height: 720px;
    background: var(--label);
    position: relative;
  }
  .frame-outer {
    position: absolute; inset: 44px;
    border: 4px solid var(--frame);
  }
  .frame-inner {
    position: absolute; inset: 56px;
    border: 1.5px solid var(--frame);
    display: flex; flex-direction: column; align-items: center;
  }
  .brand-name {
    margin-top: 92px;
    font-size: 82px; font-weight: 400; letter-spacing: 8px;
    color: var(--ink); line-height: 1;
  }
  .brand-tagline {
    margin-top: 12px;
    font-size: 17px; font-weight: 400; letter-spacing: 6px;
    color: var(--ink-soft);
  }
  .divider {
    margin-top: 48px;
    width: 440px; height: 40px;
    position: relative;
  }
  .divider svg { width: 100%; height: 100%; display: block; }
  .fragrance-name {
    margin: 14px 0;
    font-size: 38px; font-weight: 400; letter-spacing: 5px;
    color: var(--ink-soft);
  }
  .product-type {
    margin-top: 42px;
    font-size: 30px; font-weight: 300; letter-spacing: 3px;
    color: var(--ink);
  }
</style>
</head>
<body>
<main class="canvas">
  <section class="label">
    <div class="frame-outer"></div>
    <div class="frame-inner">
      <h1 class="brand-name">LIRELLE</h1>
      <p class="brand-tagline">HOME FRAGRANCE</p>

      <div class="divider">
        <svg viewBox="0 0 440 40">
          <line x1="0" y1="32" x2="440" y2="32" stroke="var(--frame)" stroke-width="2"/>
          <circle cx="4" cy="32" r="3" fill="var(--frame)"/>
          <circle cx="436" cy="32" r="3" fill="var(--frame)"/>
          <rect x="180" y="2" width="80" height="24" rx="10" fill="var(--ornament)" role="img" aria-label="Scrolled flourish ornament"/>
        </svg>
      </div>

      <h2 class="fragrance-name">ENGLISH ROSE</h2>

      <div class="divider">
        <svg viewBox="0 0 440 40">
          <line x1="0" y1="8" x2="440" y2="8" stroke="var(--frame)" stroke-width="2"/>
          <circle cx="4" cy="8" r="3" fill="var(--frame)"/>
          <circle cx="436" cy="8" r="3" fill="var(--frame)"/>
          <rect x="180" y="14" width="80" height="24" rx="10" fill="var(--ornament)" role="img" aria-label="Scrolled flourish ornament"/>
        </svg>
      </div>

      <p class="product-type">Scented Candle</p>
    </div>
  </section>
</main>
</body>
</html>
```